The Ledgerline Business Card

Business card with QR Code for an accounting and tax business

Target Market(s)

Small Business and Individual Tax

Industry/Entity Type

Bookkeeping, Accounting and Taxes

Contact Information for Business Card

482 CALDWELL ST STE 2210 #614273 BOSTON, MA Zip: 02387

Requirements
Must have
• Name and Address

```html
<!DOCTYPE html>
<html lang="en">
<head>
<meta charset="utf-8">
<title>The Ledgerline Business Card</title>
<link href="https://fonts.googleapis.com/css2?family=Arimo:wght@400;700&display=swap" rel="stylesheet">
<style>
  :root {
    --backdrop: #ecebe8;
    --card-light: #e4e3e0;
    --card-dark: #d3d1cd;
    --card-edge: #f4f3f1;
    --ink: #1f1f1f;
    --ink-soft: #4a4a4a;
    --rule: #3a3a3a;
  }
  * { margin: 0; padding: 0; box-sizing: border-box; }
  html, body {
    width: 1200px;
    height: 969px;
    overflow: hidden;
    background: var(--backdrop);
    font-family: "Arimo", Arial, sans-serif;
    color: var(--ink);
  }
  .business-card {
    position: absolute;
    left: 100px;
    top: 200px;
    width: 1000px;
    height: 568px;
    border-radius: 22px;
    background: linear-gradient(160deg, var(--card-light) 0%, var(--card-dark) 100%);
    border: 2px solid var(--card-edge);
    box-shadow: 0 18px 40px rgba(0,0,0,0.12);
  }
  .brand {
    position: absolute;
    right: 56px;
    top: 110px;
    display: flex;
    align-items: center;
    gap: 16px;
  }
  .brand-dot {
    width: 34px;
    height: 34px;
    border-radius: 50%;
    background: var(--ink);
  }
  .brand-name {
    font-size: 34px;
    font-weight: 700;
    color: var(--ink);
  }
  .person-name {
    position: absolute;
    left: 55px;
    top: 282px;
    font-size: 34px;
    font-weight: 700;
  }
  .person-title {
    position: absolute;
    left: 55px;
    top: 324px;
    font-size: 24px;
    color: var(--ink-soft);
  }
  .address {
    position: absolute;
    left: 55px;
    top: 373px;
    font-size: 25px;
    line-height: 30px;
  }
  .contact {
    position: absolute;
    left: 55px;
    top: 462px;
    display: flex;
    font-size: 24px;
    line-height: 33px;
  }
  .contact-column { padding-right: 26px; }
  .contact-column + .contact-column {
    border-left: 2px solid var(--rule);
    padding-left: 24px;
  }
  .label { font-weight: 700; }
</style>
</head>
<body>
  <section class="business-card">
    <div class="brand">
      <span class="brand-dot"></span>
      <span class="brand-name">The Ledgerline</span>
    </div>

    <h1 class="person-name">Daniel Mercer</h1>
    <p class="person-title">President</p>

    <p class="address">482 Caldwell St ste 2210 #614273 Boston<br>MA Zip: 02387</p>

    <div class="contact">
      <div class="contact-column">
        <div><span class="label">P :</span> (555) 3921-6640</div>
        <div><span class="label">C :</span> (555) 3921-6641</div>
      </div>
      <div class="contact-column">
        <div><span class="label">E :</span> name@theledgerline.com</div>
        <div><span class="label">W :</span> www.theledgerline.com</div>
      </div>
    </div>
  </section>
</body>
</html>
```